Media and Film Company Needs a New Website

We produce highly stylized commercials and film pieces for our clients. We also produce live events, both corporate and theatrical. Looking for a site that can show off our client videos - have a polished way to show off our team, and be able to create pages to highlight our clients and give a full overview of our project/process with them. We design simple website for some of our clients - so we are very wordpress familiar, and would like something that doesn't feel like a template.

Target Market(s)

content creators, creative directors, production teams, marketing agencies

Industry/Entity Type

Film Production

Number of Pages Required

4 page

Font styles to use
Sans Serif

Requirements
Must have
• slick looking video embed (from YT or Vimeo)
• project pages - client snapshot (what we did for them, how we did it)
• nice landing page, have our company video reel on the page
• testimonials
• contact page
• ability to have photos as a background if we want
Nice to have
• polished clean look - look to our logo colors and linear elements
• we produce very stylized videos for our clients and our website should reflect that
Should not have
• template look or feel to it- please bring your flare to the project!
• take a look at our current site - zantorvo.com we need a better way to highlight our work and our clients

```html
<!DOCTYPE html>
<html lang="en">
<head>
<meta charset="utf-8">
<title>Zantorvo Media &amp; Entertainment</title>
<link rel="stylesheet" href="https://fonts.googleapis.com/css2?family=Open+Sans:ital,wght@0,300;0,400;0,600;0,700;0,800;1,400&display=swap">
<style>
:root{
  --magenta:#c2307f;
  --ink:#2f2f33;
  --text:#555a60;
  --muted:#8a8f96;
  --line:#e2e2e6;
  --card-border:#e6e6ea;
  --btn-soft:#e8eef4;
  --footer:#1d1d1f;
  --footer-bar:#111113;
  --white:#ffffff;
}
*{box-sizing:border-box;margin:0;padding:0}
html,body{width:1200px;height:3797px;overflow:hidden;background:var(--white)}
body{font-family:"Open Sans",Arial,sans-serif;color:var(--text)}
.page{position:relative;width:1200px;height:3797px;overflow:hidden}
.abs{position:absolute}

/* Hero */
.hero{left:0;top:0;width:1200px;height:620px;
  background:radial-gradient(ellipse at 50% 10%,#8a6fd0 0%,#5a3f9a 25%,#2c1d4e 55%,#120c1e 100%)}
.hero-shade{left:0;top:0;width:1200px;height:620px;background:linear-gradient(180deg,rgba(0,0,0,0) 40%,rgba(0,0,0,.55) 100%)}
.menu-toggle{left:1062px;top:38px;width:30px;height:24px}
.menu-toggle span{display:block;height:3px;background:var(--white);margin-bottom:7px}
.hero-kicker{left:0;top:158px;width:1200px;text-align:center;color:var(--white);font-weight:300;font-size:52px;letter-spacing:2px}
.hero-title{left:0;top:220px;width:1200px;text-align:center;color:var(--white);font-weight:800;font-size:56px;letter-spacing:1px}
.hero-sub{left:0;top:292px;width:1200px;text-align:center;color:var(--white);font-size:14px;letter-spacing:.5px;text-transform:uppercase}
.btn{display:flex;align-items:center;justify-content:center;font-weight:700;color:var(--white);font-size:19px}
.btn-clients{left:385px;top:344px;width:200px;height:51px;background:var(--magenta)}
.btn-video{left:605px;top:344px;width:210px;height:51px;border:2px solid var(--white);gap:12px}
.hero-dots{left:568px;top:451px;width:64px;height:4px;display:flex;gap:10px}
.hero-dots span{flex:1;background:var(--white)}

/* Nav */
.navbar{left:0;top:620px;width:1200px;height:69px;background:var(--white);box-shadow:0 2px 6px rgba(0,0,0,.08)}
.brand{left:111px;top:640px;font-weight:800;font-size:26px;color:var(--ink);letter-spacing:-.5px;display:flex;align-items:center;gap:8px}
.brand small{font-size:10px;font-weight:600;color:var(--magenta);letter-spacing:.5px}
.nav-links{left:415px;top:641px;height:26px;display:flex;align-items:center;list-style:none}
.nav-links li{font-size:11px;text-transform:uppercase;color:var(--muted);padding:0 20px;line-height:26px;white-space:nowrap}
.nav-links li.active{background:var(--magenta);color:var(--white);padding:0 13px;margin-right:10px}

/* Section heads */
.section-title{left:0;width:1200px;text-align:center;font-weight:700;font-size:27px;color:var(--ink);text-transform:uppercase}
.section-title em{font-style:normal;color:var(--magenta)}
.ruled{left:111px;width:978px;display:flex;align-items:center;gap:18px;font-weight:700;font-size:27px;color:var(--ink);text-transform:uppercase}
.ruled::before,.ruled::after{content:"";flex:1;height:1px;background:var(--line)}
.ruled span{white-space:nowrap}
.ruled em{font-style:normal;color:var(--magenta)}
.title-mark{left:520px;top:799px;width:160px;height:2px;border-top:2px dotted #d9d9de}
.title-mark i{position:absolute;left:76px;top:-5px;width:8px;height:8px;border-radius:50%;background:var(--magenta)}

/* Services */
.service{width:228px;height:349px;top:904px;border:1px solid var(--card-border);text-align:center}
.service.featured{border-color:var(--magenta)}
.service-icon{position:absolute;left:73px;top:-43px;width:82px;height:82px;border:1px solid var(--card-border);background:var(--white);display:flex;align-items:center;justify-content:center}
.service.featured .service-icon{background:var(--magenta);border-color:var(--magenta);border-radius:4px}
.service h3{position:absolute;top:62px;left:0;width:100%;font-size:11px;font-weight:700;color:var(--ink);line-height:15px;text-transform:uppercase}
.service ul{position:absolute;top:115px;left:0;width:100%;list-style:none}
.service li{font-size:10.5px;text-transform:uppercase;color:var(--text);height:40px;line-height:14px}
.service .go{position:absolute;left:39px;top:278px;width:150px;height:38px;background:var(--btn-soft);color:#6d7781;font-size:11px;display:flex;align-items:center;justify-content:center;text-transform:uppercase}
.service.featured .go{background:var(--magenta);color:var(--white)}

/* Works */
.works-grid{left:111px;top:1428px;width:978px;height:810px;display:grid;grid-template-columns:repeat(3,1fr);grid-template-rows:repeat(3,1fr);gap:10px}
.shot{position:relative}
.shot-1{background:linear-gradient(135deg,#4c4a48,#1c1b1a 70%,#7a5a3c)}
.shot-2{background:linear-gradient(135deg,#9b7b63,#d9c3a9 55%,#6b4f3f)}
.shot-3{background:linear-gradient(135deg,#2a2f3a,#5b6678 55%,#1b1e26)}
.shot-4{background:linear-gradient(135deg,#e9d7c3,#a38a73 60%,#f2e6d9)}
.shot-5{background:linear-gradient(135deg,#7a6a58,#3a2e25)}
.shot-6{background:linear-gradient(135deg,#3c2f2a,#8d6c55 55%,#c9b8a8)}
.shot-7{background:linear-gradient(135deg,#6e6a66,#2b2826 60%,#4e4844)}
.shot-8{background:linear-gradient(135deg,#8d939a,#3a3d42 55%,#c6cacf)}
.shot-9{background:linear-gradient(135deg,#2b2d30,#7c8086 55%,#1a1b1d)}
.shot-overlay{position:absolute;inset:0;background:rgba(194,48,127,.85);display:flex;flex-direction:column;align-items:center;padding-top:50px}
.shot-overlay::after{content:"";position:absolute;inset:14px;border:1px solid rgba(255,255,255,.55)}
.shot-overlay p{color:var(--white);font-size:15px;text-align:center;width:220px;line-height:20px}
.round-icon{width:82px;height:82px;border-radius:50%;background:var(--white);display:flex;align-items:center;justify-content:center;margin-top:40px}

/* Feature photos */
.feature-desc{left:190px;top:2363px;width:820px;text-align:center;font-size:14px;line-height:20px;color:var(--text)}
.feature-row{left:111px;top:2448px;width:978px;height:231px;display:grid;grid-template-columns:repeat(4,1fr);gap:17px}
.tile{position:relative;display:flex;align-items:center;justify-content:center}
.tile-cta{background:linear-gradient(135deg,#e06aae,#c2307f);flex-direction:column;gap:18px}
.tile-cta .pair{display:flex;gap:10px}
.tile-cta .pair span{width:32px;height:32px;border-radius:50%;background:rgba(0,0,0,.25);display:flex;align-items:center;justify-content:center}
.tile-cta strong{color:var(--white);font-size:14px;font-weight:700}
.tile-2{background:linear-gradient(135deg,#2c3a5c,#6c6f7a 55%,#1c2134)}
.tile-3{background:linear-gradient(135deg,#b3a48f,#6f6353 55%,#d9cab6)}
.tile-4{background:linear-gradient(135deg,#f1efec,#bdb6b0 45%,#a82a2a)}
.tile .round-icon{margin:0;width:62px;height:62px;background:rgba(255,255,255,.9)}
.btn-portfolio{left:480px;top:2727px;width:240px;height:53px;background:var(--magenta);color:var(--white);font-size:16px;font-weight:700;text-transform:uppercase;display:flex;align-items:center;justify-content:center}

/* Testimonials */
.avatar{left:549px;top:2937px;width:102px;height:102px;border-radius:50%;background:linear-gradient(160deg,#c9b9a8,#6a5a4a)}
.quote{left:180px;top:3076px;width:840px;text-align:center;font-style:italic;font-size:17px;line-height:23px;color:var(--muted)}
.quote-name{left:0;top:3150px;width:1200px;text-align:center;font-size:17px;color:var(--ink);text-transform:uppercase}
.arrow{top:3076px;width:20px;height:30px}

/* Clients */
.client-arrows{left:1058px;top:3332px;display:flex;gap:6px}
.client-row{left:111px;top:3362px;width:978px;height:84px;display:grid;grid-template-columns:repeat(6,1fr);gap:20px}
.client{border:1px solid var(--card-border);display:flex;align-items:center;justify-content:center;font-size:15px;font-weight:700;color:var(--ink);white-space:nowrap}

/* Footer */
.footer{left:0;top:3555px;width:1200px;height:192px;background:var(--footer)}
.footer-cta{left:0;top:3592px;width:1200px;text-align:center;color:var(--white);font-size:22px;font-weight:700;text-transform:uppercase}
.footer-mail{left:180px;top:3662px;display:flex;align-items:center;gap:28px;color:var(--white);font-size:22px}
.footer-social{left:605px;top:3666px;display:flex;align-items:center;gap:8px;color:var(--white);font-size:22px}
.footer-social span{width:36px;height:36px;border-radius:50%;background:var(--white)}
.footer-social p{margin-left:18px}
.footer-bar{left:0;top:3747px;width:1200px;height:50px;background:var(--footer-bar)}
.footer-links{left:111px;top:3762px;display:flex;gap:24px;list-style:none;color:var(--white);font-size:13px}
.copyright{left:740px;top:3763px;width:300px;text-align:right;color:var(--white);font-size:11px;text-transform:uppercase}
.to-top{left:1055px;top:3757px;width:30px;height:30px;border:2px solid var(--white);border-radius:50%;display:flex;align-items:center;justify-content:center}
</style>
</head>
<body>
<div class="page">

  <header>
    <div class="abs hero" role="img" aria-label="Concert crowd with raised hands under purple stage lights"></div>
    <div class="abs hero-shade"></div>
    <div class="abs menu-toggle" aria-label="Menu"><span></span><span></span><span></span></div>
    <div class="abs hero-kicker">ZANTORVO</div>
    <h1 class="abs hero-title">MEDIA &amp; ENTERTAINMENT</h1>
    <p class="abs hero-sub">Live Entertainment &amp; Theatrical Production</p>
    <a class="abs btn btn-clients">Our Clients</a>
    <a class="abs btn btn-video">
      <svg width="22" height="14" viewBox="0 0 22 14"><rect x="0" y="1" width="14" height="12" rx="2" fill="#fff"/><path d="M15 7 L22 2 L22 12 Z" fill="#fff"/></svg>
      Watch video
    </a>
    <div class="abs hero-dots"><span></span><span></span></div>
  </header>

  <nav>
    <div class="abs navbar"></div>
    <div class="abs brand">ZANTORVO <small>&amp; ENTERTAINMENT</small></div>
    <ul class="abs nav-links">
      <li class="active">Home</li>
      <li>About Zantorvo</li>
      <li>Portfolio</li>
      <li>Testimonials</li>
      <li>Press</li>
      <li>Our Clients</li>
      <li>Contacts</li>
    </ul>
  </nav>

  <section>
    <h2 class="abs section-title" style="top:752px">What <em>we do</em></h2>
    <div class="abs title-mark"><i></i></div>

    <div class="abs service" style="left:111px">
      <div class="service-icon">
        <svg width="44" height="44" viewBox="0 0 44 44" fill="none" stroke="#555" stroke-width="2"><circle cx="20" cy="20" r="16"/><circle cx="20" cy="20" r="3"/><circle cx="20" cy="10" r="4"/><circle cx="20" cy="30" r="4"/><circle cx="10" cy="20" r="4"/><circle cx="30" cy="20" r="4"/><path d="M30 36 H42"/></svg>
      </div>
      <h3>Film &amp;<br>Media Production</h3>
      <ul><li>Pro Editing Suite</li><li>Motion Graphics</li><li>4K Workflow</li><li>Direct to Web/Streaming</li></ul>
      <a class="go">Get to work</a>
    </div>

    <div class="abs service featured" style="left:360px">
      <div class="service-icon">
        <svg width="44" height="44" viewBox="0 0 44 44" fill="none" stroke="#fff" stroke-width="2"><rect x="4" y="14" width="26" height="20" rx="2"/><circle cx="17" cy="24" r="6"/><rect x="22" y="4" width="18" height="14" rx="2"/><circle cx="31" cy="11" r="3"/></svg>
      </div>
      <h3>Live<br>Production</h3>
      <ul><li>Theatrical Producing</li><li>Production Management</li><li>Lighting &amp; Video Design</li><li>Audio System Design</li></ul>
      <a class="go">Get to work</a>
    </div>

    <div class="abs service" style="left:608px">
      <div class="service-icon">
        <svg width="44" height="44" viewBox="0 0 44 44" fill="none" stroke="#555" stroke-width="2"><rect x="12" y="4" width="20" height="12"/><rect x="6" y="16" width="32" height="16" rx="2"/><rect x="12" y="26" width="20" height="14"/><path d="M16 32 H28 M16 36 H26"/></svg>
      </div>
      <h3>PR,<br>Marketing &amp; Advertising</h3>
      <ul><li>Branding</li><li>Social Media</li><li>Media Relations and Outreach</li><li>Street Teams</li></ul>
      <a class="go">Get to work</a>
    </div>

    <div class="abs service" style="left:856px">
      <div class="service-icon">
        <svg width="44" height="44" viewBox="0 0 44 44" fill="none" stroke="#555" stroke-width="2"><rect x="4" y="14" width="36" height="24" rx="3"/><circle cx="14" cy="26" r="6"/><path d="M26 22 H34 M26 27 H34 M26 32 H34 M10 14 L30 4"/></svg>
      </div>
      <h3>Our<br>Events</h3>
      <ul><li>Event Production</li><li>Staffing &amp; Hiring</li><li>Manage RFPs</li><li>Sponsor Relations</li></ul>
      <a class="go">Get to work</a>
    </div>
  </section>

  <section>
    <h2 class="abs ruled" style="top:1354px"><span>Our <em>Works</em></span></h2>
    <div class="abs works-grid">
      <div class="shot shot-1" role="img" aria-label="Film clapperboard and reel on a studio table"></div>
      <div class="shot shot-2" role="img" aria-label="Group of friends watching on a sofa"></div>
      <div class="shot shot-3" role="img" aria-label="Camera operator filming a live studio audience"></div>
      <div class="shot shot-4" role="img" aria-label="Young man with headphones using a phone"></div>
      <div class="shot shot-5" role="img" aria-label="Project highlight">
        <div class="shot-overlay">
          <p>Zantorvo Media &amp; Entertainment works to build strong relationships.</p>
          <div class="round-icon">
            <svg width="30" height="30" viewBox="0 0 30 30" fill="none" stroke="#c2307f" stroke-width="3"><rect x="3" y="12" width="14" height="7" rx="3.5" transform="rotate(-45 10 15)"/><rect x="13" y="12" width="14" height="7" rx="3.5" transform="rotate(-45 20 15)"/></svg>
          </div>
        </div>
      </div>
      <div class="shot shot-6" role="img" aria-label="Person editing video on a laptop"></div>
      <div class="shot shot-7" role="img" aria-label="Family watching a demo reel on a wall screen"></div>
      <div class="shot shot-8" role="img" aria-label="Close view of studio headphones"></div>
      <div class="shot shot-9" role="img" aria-label="Hands on an audio mixing desk"></div>
    </div>
  </section>

  <section>
    <h2 class="abs ruled" style="top:2311px"><span>Our <em>Feature Photo</em></span></h2>
    <p class="abs feature-desc">Zantorvo Media &amp; Entertainment provides full-service campaigns in film and media production, live entertainment &amp; theatrical production, marketing &amp; advertising, and event management in the DC metro area.</p>
    <div class="abs feature-row">
      <div class="tile tile-cta">
        <div class="pair">
          <span><svg width="16" height="16" viewBox="0 0 30 30" fill="none" stroke="#fff" stroke-width="4"><rect x="3" y="12" width="14" height="7" rx="3.5" transform="rotate(-45 10 15)"/><rect x="13" y="12" width="14" height="7" rx="3.5" transform="rotate(-45 20 15)"/></svg></span>
          <span><svg width="16" height="16" viewBox="0 0 16 16" fill="none" stroke="#fff" stroke-width="2"><circle cx="7" cy="7" r="4.5"/><path d="M10.5 10.5 L14 14"/></svg></span>
        </div>
        <strong>SEE OUR PORTFOLIO</strong>
      </div>
      <div class="tile tile-2" role="img" aria-label="Speaker at a podium during a formal event"><div class="round-icon"><svg width="24" height="24" viewBox="0 0 30 30" fill="none" stroke="#555" stroke-width="3"><rect x="3" y="12" width="14" height="7" rx="3.5" transform="rotate(-45 10 15)"/><rect x="13" y="12" width="14" height="7" rx="3.5" transform="rotate(-45 20 15)"/></svg></div></div>
      <div class="tile tile-3" role="img" aria-label="Guests mingling at a reception"><div class="round-icon"><svg width="24" height="24" viewBox="0 0 30 30" fill="none" stroke="#555" stroke-width="3"><rect x="3" y="12" width="14" height="7" rx="3.5" transform="rotate(-45 10 15)"/><rect x="13" y="12" width="14" height="7" rx="3.5" transform="rotate(-45 20 15)"/></svg></div></div>
      <div class="tile tile-4" role="img" aria-label="Lounge set with red chairs and a screen"><div class="round-icon"><svg width="24" height="24" viewBox="0 0 30 30" fill="none" stroke="#555" stroke-width="3"><rect x="3" y="12" width="14" height="7" rx="3.5" transform="rotate(-45 10 15)"/><rect x="13" y="12" width="14" height="7" rx="3.5" transform="rotate(-45 20 15)"/></svg></div></div>
    </div>
    <a class="abs btn-portfolio">See our portfolio</a>
  </section>

  <section>
    <h2 class="abs ruled" style="top:2863px"><span>Testi<em>monials</em></span></h2>
    <div class="abs avatar" role="img" aria-label="Client portrait"></div>
    <svg class="abs arrow" style="left:112px" viewBox="0 0 20 30" fill="none" stroke="#9aa0a6" stroke-width="3"><path d="M15 5 L5 15 L15 25"/></svg>
    <p class="abs quote">Thank you very much for all the hard work and creativity that you devoted to the PCR video, which was moving and uplifting and captured the essence of what we try to do so very well.</p>
    <svg class="abs arrow" style="left:1068px" viewBox="0 0 20 30" fill="none" stroke="#c2307f" stroke-width="3"><path d="M5 5 L15 15 L5 25"/></svg>
    <p class="abs quote-name">Marla Ostrand</p>
  </section>

  <section>
    <h2 class="abs ruled" style="top:3273px"><span>Our <em>Clients</em></span></h2>
    <div class="abs client-arrows">
      <svg width="10" height="14" viewBox="0 0 10 14" fill="none" stroke="#c2307f" stroke-width="2"><path d="M8 2 L3 7 L8 12"/></svg>
      <svg width="10" height="14" viewBox="0 0 10 14" fill="none" stroke="#c2307f" stroke-width="2"><path d="M2 2 L7 7 L2 12"/></svg>
    </div>
    <div class="abs client-row">
      <div class="client">Reelmark</div>
      <div class="client">Norvend</div>
      <div class="client">Kalthra</div>
      <div class="client">Brisvale</div>
      <div class="client">Tunequill</div>
      <div class="client">Verdana Path</div>
    </div>
  </section>

  <footer>
    <div class="abs footer"></div>
    <p class="abs footer-cta">Ready to get to work? Contact us today</p>
    <div class="abs footer-mail">
      <svg width="48" height="44" viewBox="0 0 48 44" fill="none" stroke="#fff" stroke-width="2.5"><rect x="3" y="14" width="42" height="28" rx="2"/><path d="M3 14 L24 30 L45 14 M10 14 V3 H38 V14 M16 10 H32 M16 16 H32"/></svg>
      info@zantorvo.com
    </div>
    <div class="abs footer-social">
      <span></span><span></span><span></span><span></span><span></span><span></span>
      <p>We are social</p>
    </div>
    <div class="abs footer-bar"></div>
    <ul class="abs footer-links"><li>Home</li><li>About us</li><li>Our Clients</li><li>News</li><li>Contact us</li></ul>
    <p class="abs copyright">©2017 Zantorvo Media &amp; Entertainment</p>
    <div class="abs to-top"><svg width="12" height="14" viewBox="0 0 12 14" fill="none" stroke="#fff" stroke-width="2"><path d="M6 13 V2 M1 7 L6 2 L11 7"/></svg></div>
  </footer>

</div>
</body>
</html>
```